ZEPRILO.COM is a premium domain sales company. Our competitors are companies like vastplots.example, getparcels.example, peerwords.example. Our current site is at www.zeprilos.example.

We want to have the ability to search for domains, to highlight special offers and have some testimonials on the index page.

The logo for the site is attached.

Please be sure that the order form fits on the screen without scrolling the page. I want the entire form, including the submit button to fit without any page scrolling.

Delivered product - INDEX PAGE, ORDER FORM AND CONTENT PAGE PSDs.

Target Market(s)

Small to Medium business professionals

Industry/Entity Type

It Company

Requirements
Must have
• 1. List of domains for sale
2. Simple search box with button to run the search
3. link for advanced search
4. testimonial area. Note - this can be a small box where a different testimonial is displayed on each page load.
Nice to have
• Would like the site to have some white space. Don't want a heavily packed website. Give it an "airy" feel.

```html
<!DOCTYPE html>
<html lang="en">
<head>
<meta charset="utf-8">
<title>ZEPRILO.COM – Premium Domains</title>
<link rel="stylesheet" href="https://fonts.googleapis.com/css2?family=Caveat:wght@400;600&family=Merriweather:ital,wght@1,400;1,700&family=Open+Sans:ital,wght@0,300;0,400;0,600;0,700;1,400;1,600&display=swap">
<style>
:root{
  --blue:#1d5aa6;
  --blue-dark:#123f7e;
  --brand-blue:#0b4f9c;
  --green:#6aaf35;
  --green-light:#8cc63f;
  --orange:#f7a800;
  --orange-text:#f5a300;
  --grey-band:#8a8a8a;
  --grey-text:#6d6d6d;
  --white:#ffffff;
}
*{margin:0;padding:0;box-sizing:border-box}
html,body{width:1062px;height:1200px;overflow:hidden;background:var(--white)}
body{position:relative;font-family:"Open Sans",sans-serif;color:#333}
.abs{position:absolute}

/* header */
.site-header{left:0;top:0;width:1062px;height:111px;background:linear-gradient(180deg,#1f5fae 0%,#17498c 100%)}
.logo{font-weight:700;font-size:27px;letter-spacing:-0.5px;white-space:nowrap}
.logo--header{left:106px;top:32px;color:var(--white)}
.main-nav a{position:absolute;top:44px;color:var(--white);font-weight:700;font-size:14.5px;text-decoration:none;letter-spacing:-0.3px}
.main-nav a.is-active{top:37px;left:346px;width:69px;height:33px;background:var(--white);color:var(--blue-dark);text-align:center;line-height:33px}
.offer-badge{left:764px;top:13px;width:84px;height:84px;border-radius:50%;background:var(--orange);border:3px dashed #ffc640;color:var(--white);text-align:center;font-weight:700}
.offer-badge .price{display:block;font-size:22px;margin-top:18px;line-height:1}
.offer-badge .sub{display:block;font-size:8px}
.offer-badge .ribbon{display:block;margin:4px auto 0;width:74px;background:var(--blue-dark);font-size:7.5px;padding:2px 0}
.account-links{right:106px;top:26px;text-align:right}
.account-links a{display:block;color:var(--orange-text);font-size:13.5px;font-weight:600;text-decoration:none;line-height:20.5px}
.account-links svg{vertical-align:-2px;margin-left:4px}

/* hero */
.hero{left:0;top:111px;width:1062px;height:410px;background:linear-gradient(90deg,#151515 0%,#2a2a2a 45%,#4a4a4a 100%);overflow:hidden}
.hero-photo{left:540px;top:0;width:522px;height:380px;background:linear-gradient(160deg,#cfc4b4 0%,#6f7a8a 45%,#2c3f60 100%);opacity:.9}
.hero-band{left:0;top:0;width:1062px;height:410px}
.hero-title{left:106px;top:190px;font-family:"Caveat",cursive;font-weight:600;font-size:56px;color:var(--green);line-height:1;white-space:nowrap}
.hero-sub{left:105px;top:255px;font-weight:300;font-size:21px;color:var(--white);letter-spacing:-0.6px;white-space:nowrap}
.search{left:107px;top:296px;width:479px;height:69px;background:var(--white);border-radius:8px;box-shadow:0 0 0 2px rgba(255,255,255,.5)}
.search__input{left:20px;top:20px;font-size:22px;color:#777;font-weight:400}
.search__tld{left:339px;top:3px;width:73px;height:63px;background:#d9d9d9;color:#777;font-style:italic;font-weight:700;font-size:14px;line-height:63px;text-align:center}
.search__go{left:412px;top:3px;width:64px;height:63px;background:linear-gradient(180deg,var(--green-light),#6aa92c);border-radius:0 6px 6px 0;color:var(--white);font-weight:700;font-size:28px;line-height:63px;text-align:center}
.search-hint{left:105px;top:375px;font-size:10px;font-style:italic;font-weight:600;color:var(--white);white-space:nowrap}
.adv-search{left:467px;top:374px;font-size:13px;color:var(--orange-text);white-space:nowrap}
.phone-icon{left:107px;top:416px}
.phone-number{left:142px;top:410px;font-size:29px;color:var(--white);font-style:italic;letter-spacing:-1px;white-space:nowrap}
.inquiry{left:387px;top:448px;font-size:12px;color:var(--white)}

.special-tab{left:0;top:262px;width:45px;height:186px;background:var(--orange);border-radius:0 3px 3px 0}
.special-tab span{position:absolute;left:50%;top:50%;transform:translate(-50%,-50%) rotate(-90deg);white-space:nowrap;color:var(--white);font-size:21px;font-weight:400}

/* testimonials */
.section-title{left:0;top:556px;width:1062px;text-align:center;font-family:"Caveat",cursive;font-weight:600;font-size:46px;color:var(--brand-blue)}
.section-sub{left:0;top:620px;width:1062px;text-align:center;font-size:11.5px;color:#222}
.section-sub::before,.section-sub::after{content:"";display:inline-block;width:86px;height:4px;border-top:1px solid #ccc;border-bottom:1px solid #ccc;vertical-align:middle;margin:0 4px}
.testimonial{top:692px;width:290px;height:120px}
.testimonial__thumb{left:2px;top:2px;width:58px;height:68px;border-radius:50%;border:3px solid #f1f1f1;box-shadow:0 2px 4px rgba(0,0,0,.3)}
.testimonial__site{left:72px;top:3px;font-size:17.5px;color:var(--brand-blue);white-space:nowrap}
.testimonial__name{left:72px;top:30px;font-family:"Merriweather",serif;font-style:italic;font-weight:700;font-size:12.5px;color:#333;white-space:nowrap}
.testimonial__text{left:72px;top:47px;width:220px;font-family:"Merriweather",serif;font-style:italic;font-size:10.5px;line-height:14px;color:#555}
.testimonial__date{left:72px;top:100px;font-family:"Caveat",cursive;font-size:18px;color:var(--orange-text);white-space:nowrap}
.testimonial__date b{color:#bbb;font-family:Georgia,serif;font-size:22px;margin-right:6px}

/* stats */
.stats{left:0;top:875px;width:1062px;height:106px;background:var(--grey-band)}
.stat{top:27px;font-weight:300;font-size:31px;line-height:26px;color:#e6e6e6;text-align:center;letter-spacing:-0.5px;white-space:nowrap}
.stat-tag{top:0;height:18px;background:var(--orange);color:var(--white);font-size:10px;font-weight:600;text-align:center;line-height:18px;border-radius:0 0 2px 2px}
.stat-sep{top:53px;width:18px;height:1px;background:#cfcfcf}

/* footer */
.logo--footer{left:106px;top:1055px;color:var(--brand-blue)}
.copyright{left:110px;top:1096px;font-size:11px;line-height:14px;color:var(--grey-text);letter-spacing:.3px}
.footer-links{top:1046px}
.footer-links li{list-style:none;font-size:11px;color:var(--grey-text);line-height:20px;letter-spacing:.3px;white-space:nowrap}
.footer-links li::before{content:"→";color:#bbb;font-size:9px;margin-right:6px}
.call-title{left:620px;top:1040px;font-size:22px;line-height:28px;color:var(--brand-blue);letter-spacing:-0.6px;white-space:nowrap}
.call-numbers{left:800px;top:1043px;font-size:19px;line-height:27px;color:var(--grey-text);font-style:italic;letter-spacing:-1px;white-space:nowrap}
.footer-rule{left:620px;top:1112px;width:336px;height:1px;background:#ccc}
.we-accept{left:620px;top:1122px;font-family:"Caveat",cursive;font-size:26px;color:var(--grey-text)}
.cards{left:756px;top:1129px;display:flex;gap:4px}
.cards span{display:block;width:38px;height:22px;border-radius:2px}
</style>
</head>
<body>

<header class="site-header abs">
  <div class="logo logo--header abs">ZEPRILO.COM</div>
  <nav class="main-nav">
    <a class="is-active" href="#">HOME</a>
    <a href="#" style="left:437px">CATEGORIES</a>
    <a href="#" style="left:543px">FAQS</a>
    <a href="#" style="left:598px">ABOUT</a>
    <a href="#" style="left:668px">CONTACT</a>
  </nav>
  <div class="offer-badge abs">
    <span class="price">$10</span>
    <span class="sub">ONLY</span>
    <span class="ribbon">SPACIAL OFFER</span>
  </div>
  <div class="account-links abs">
    <a href="#">MyCart<svg width="14" height="12" viewBox="0 0 14 12"><path d="M0 1h3l2 7h7l2-5H4" fill="none" stroke="#f5a300" stroke-width="1.6"/><circle cx="6" cy="10.5" r="1.2" fill="#f5a300"/><circle cx="11" cy="10.5" r="1.2" fill="#f5a300"/></svg></a>
    <a href="#">My Account<svg width="12" height="12" viewBox="0 0 12 12"><circle cx="6" cy="3.5" r="3" fill="#f5a300"/><path d="M0 12c0-4 3-5 6-5s6 1 6 5z" fill="#f5a300"/></svg></a>
    <a href="#">More Offers<svg width="12" height="12" viewBox="0 0 12 12"><circle cx="6" cy="6" r="6" fill="#f5a300"/><path d="M5 3l3 3-3 3" fill="none" stroke="#17498c" stroke-width="1.6"/></svg></a>
  </div>
</header>

<section class="hero abs">
  <div class="hero-photo abs" role="img" aria-label="Photo of a smiling couple looking at a laptop together in front of server racks"></div>
  <svg class="hero-band abs" viewBox="0 0 1062 410" preserveAspectRatio="none">
    <polygon points="0,395 1062,360 1062,410 0,410" fill="#ffffff"/>
    <polygon points="0,398 1062,362 1062,374 0,408" fill="#5d9e32"/>
  </svg>
</section>

<div class="hero-title abs">Your Business Starts Here</div>
<div class="hero-sub abs">BUY A PREMIUM DOMAIN AND OPEN YOUR DOORS</div>

<form class="search abs">
  <div class="search__input abs">Enter your domain</div>
  <div class="search__tld abs">.COM ◤</div>
  <div class="search__go abs">GO</div>
</form>
<div class="search-hint abs">Start your search by entering the first character of the domain name.</div>
<a class="adv-search abs">Advanced Search <svg width="11" height="11" viewBox="0 0 12 12" style="vertical-align:-1px"><circle cx="6" cy="6" r="6" fill="#f5a300"/><path d="M5 3l3 3-3 3" fill="none" stroke="#222" stroke-width="1.6"/></svg></a>

<svg class="phone-icon abs" width="28" height="28" viewBox="0 0 28 28">
  <circle cx="14" cy="14" r="12.5" fill="none" stroke="#fff" stroke-width="2"/>
  <path d="M10 8c-1 1-1.5 2-1 3.5 1 3 4 6.5 7.5 8 1.5.5 2.5 0 3.5-1l-2.2-2.2-1.8 1c-1.5-.8-3.5-2.8-4.3-4.3l1-1.8z" fill="#fff"/>
</svg>
<div class="phone-number abs">555-277-ZEPRILO</div>
<div class="inquiry abs">Call us for inquiry</div>

<div class="special-tab abs"><span>Special Offer</span></div>

<h2 class="section-title abs">Testimonials</h2>
<div class="section-sub abs">WHAT PEOPLE ARE SAYING ABOUT US.</div>

<article class="testimonial abs" style="left:106px">
  <div class="testimonial__thumb abs" role="img" aria-label="Website thumbnail with a lake at dusk" style="background:linear-gradient(180deg,#d8c9a0,#3b4a3a 60%,#1c2a3a)"></div>
  <div class="testimonial__site abs">brightsprout.example</div>
  <div class="testimonial__name abs">Milo - Australia</div>
  <p class="testimonial__text abs">Lorem ipsum dolor sit amet, consectetur adipisicing elit, sed do eiusmod tempor incididunt</p>
  <div class="testimonial__date abs"><b>❝</b>June 15, 2011, 3p.m</div>
</article>
<article class="testimonial abs" style="left:403px">
  <div class="testimonial__thumb abs" role="img" aria-label="Website thumbnail of a dark domain search page" style="background:linear-gradient(180deg,#5a4a3a,#2a241e)"></div>
  <div class="testimonial__site abs">getparcels.example</div>
  <div class="testimonial__name abs">Greta - United Kingdom</div>
  <p class="testimonial__text abs">Lorem ipsum dolor sit amet, consectetur adipisicing elit, sed do eiusmod tempor incididunt</p>
  <div class="testimonial__date abs"><b>❝</b>June 15, 2011, 3p.m</div>
</article>
<article class="testimonial abs" style="left:705px">
  <div class="testimonial__thumb abs" role="img" aria-label="Website thumbnail with a light blue seaside scene" style="background:linear-gradient(180deg,#f3f6f8,#bfe0f2 55%,#7cc4ea)"></div>
  <div class="testimonial__site abs">peerwords.example</div>
  <div class="testimonial__name abs">Nadia - United State</div>
  <p class="testimonial__text abs">Lorem ipsum dolor sit amet, consectetur adipisicing elit, sed do eiusmod tempor incididunt</p>
  <div class="testimonial__date abs"><b>❝</b>June 15, 2011, 3p.m</div>
</article>

<section class="stats abs">
  <div class="stat-tag abs" style="left:140px;width:45px">OVER</div>
  <div class="stat abs" style="left:104px;text-align:left">350,000<br>Domains</div>
  <div class="stat-sep abs" style="left:268px"></div>
  <div class="stat-tag abs" style="left:380px;width:45px">100%</div>
  <div class="stat abs" style="left:320px;width:166px">Satisfaction<br>Guarantee</div>
  <div class="stat-sep abs" style="left:520px"></div>
  <div class="stat abs" style="left:560px;width:166px">World Class<br>Guarantee</div>
  <div class="stat-sep abs" style="left:762px"></div>
  <div class="stat abs" style="left:800px;width:166px">Trusted<br>And Secure</div>
</section>

<footer>
  <div class="logo logo--footer abs">ZEPRILO.COM</div>
  <div class="copyright abs">All Right Reseved © 2013<br>Privacy Policy &nbsp;|&nbsp; Terms</div>
  <ul class="footer-links abs" style="left:305px">
    <li>Home</li><li>Categories</li><li>Faq's</li><li>About Us</li><li>Contact Us</li>
  </ul>
  <ul class="footer-links abs" style="left:424px">
    <li>Traffic Score</li><li>Domain Rank</li><li>Popularity Score</li><li>US Based Traffic Percent</li><li>Testimonials</li>
  </ul>
  <div class="call-title abs">Call Our Domain<br>Experts Today</div>
  <div class="call-numbers abs">555-277-ZEPRILO<br>555-288-ZEPRILO</div>
  <div class="footer-rule abs"></div>
  <div class="we-accept abs">We Accept</div>
  <div class="cards abs" aria-label="Accepted payment cards">
    <span style="background:#f2a33a"></span>
    <span style="background:#c9302c"></span>
    <span style="background:#3d8fc9"></span>
    <span style="background:#e9e9e9"></span>
    <span style="background:#dfe6ef"></span>
  </div>
</footer>

</body>
</html>
```